Cosmetic injections clinic needs a fresh looking business card

We need a business card using the supplied logo and color scheme to attract future clients to our clinic. It should be modern and fresh, eye catching and not too busy. Simple and to the point is best. I would like two sided designs with the front indicating address and contact information, and the back in full color with white logo and descriptive information also provided.
Target Market(s)
Clients looking for non surgical beauty enhancements.
Contact Information for Business Card
MeloraSkin
14, 618 Birchmont Way
St. Albert, Alberta
K2P 7W3
Phone: 587-412-6630
Email: info@meloraskin.com
Requirements
Must have
- -Logo supplied with the name and address of the clinic
- -Back of card in full color with white logo with A small line of text indicating both of the following: Anti aging consultants and cosmetic injectables
- Located inside the Voyager Wellness Group

```html
<!DOCTYPE html>
<html lang="en">
<head>
<meta charset="utf-8">
<title>MeloraSkin Business Card</title>
<link rel="stylesheet" href="https://fonts.googleapis.com/css2?family=Arimo:wght@400;700&display=swap">
<style>
  :root {
    --backdrop: #ecebee;
    --magenta: #d6198f;
    --magenta-light: #e94fb3;
    --magenta-deep: #b0107a;
    --purple: #6a2c91;
    --white: #ffffff;
    --ink: #3a3a3a;
    --shadow: rgba(40, 10, 40, 0.18);
  }
  * { margin: 0; padding: 0; box-sizing: border-box; }
  html, body {
    width: 1200px; height: 799px; overflow: hidden;
    background: var(--backdrop);
    font-family: "Arimo", Arial, sans-serif;
  }
  .stage {
    position: relative; width: 1200px; height: 799px;
    display: flex; align-items: center; justify-content: center; gap: 60px;
  }
  .card {
    position: relative; width: 520px; height: 297px;
    border-radius: 22px; overflow: hidden;
    box-shadow: 0 10px 28px var(--shadow);
    background: var(--white);
  }
  .pattern-fill {
    position: absolute; inset: 0;
    background:
      radial-gradient(circle at 25% 30%, var(--magenta-light), transparent 55%),
      radial-gradient(circle at 80% 75%, var(--magenta-deep), transparent 60%),
      linear-gradient(135deg, var(--magenta-light), var(--magenta) 50%, var(--magenta-deep));
  }

  /* Back side */
  .card-back .brand {
    position: absolute; top: 108px; left: 0; right: 0;
    display: flex; align-items: center; justify-content: center; gap: 10px;
    color: var(--white);
  }
  .brand-dot { width: 26px; height: 26px; border-radius: 50%; background: currentColor; }
  .brand-name { font-weight: 700; font-size: 38px; letter-spacing: 0.5px; }
  .card-back .tagline {
    position: absolute; top: 162px; left: 0; right: 0; text-align: center;
    color: var(--white); font-weight: 700; font-size: 15px;
  }

  /* Front side */
  .card-front .band {
    position: absolute; left: 0; right: 0; top: 150px; bottom: 0;
  }
  .card-front .brand {
    position: absolute; top: 50px; left: 0; right: 0;
    display: flex; align-items: center; justify-content: center; gap: 10px;
    color: var(--purple);
  }
  .card-front .brand-name { font-size: 32px; }
  .card-front .brand-dot { width: 22px; height: 22px; background: var(--magenta); }
  .contact {
    position: absolute; display: flex; align-items: center; gap: 6px;
    color: var(--ink); font-size: 13px;
  }
  .contact-email { top: 116px; right: 22px; }
  .contact-phone { top: 124px; left: 22px; }
  .contact-icon { width: 16px; height: 16px; flex: none; }
  .person {
    position: absolute; top: 172px; left: 170px; right: 40px; text-align: center; color: var(--white);
  }
  .person-name { font-weight: 700; font-size: 32px; line-height: 1.05; }
  .person-title { font-size: 18px; margin-top: 2px; }
  .address {
    position: absolute; bottom: 20px; left: 0; right: 0; text-align: center;
    color: var(--white); font-size: 13px;
  }
</style>
</head>
<body>
<main class="stage">
  <section class="card card-back" aria-label="Card back">
    <div class="pattern-fill" role="img" aria-label="Magenta low-poly faceted background pattern"></div>
    <div class="brand">
      <span class="brand-dot"></span>
      <span class="brand-name">MeloraSkin</span>
    </div>
    <p class="tagline">Anti aging consultants and cosmetic injectables</p>
  </section>

  <section class="card card-front" aria-label="Card front">
    <div class="band pattern-fill" role="img" aria-label="Magenta low-poly faceted background pattern"></div>
    <div class="brand">
      <span class="brand-dot"></span>
      <span class="brand-name">MeloraSkin</span>
    </div>
    <div class="contact contact-email">
      <svg class="contact-icon" viewBox="0 0 16 16" aria-hidden="true">
        <circle cx="8" cy="8" r="8" fill="var(--purple)"/>
        <rect x="4" y="5.2" width="8" height="5.6" rx="0.6" fill="none" stroke="#fff" stroke-width="1"/>
        <path d="M4.2 5.6 L8 8.4 L11.8 5.6" fill="none" stroke="#fff" stroke-width="1"/>
      </svg>
      <span>info@meloraskin.com</span>
    </div>
    <div class="contact contact-phone">
      <svg class="contact-icon" viewBox="0 0 16 16" aria-hidden="true">
        <circle cx="8" cy="8" r="8" fill="var(--purple)"/>
        <path d="M5.4 4.3 L6.8 4.3 L7.3 6.3 L6.4 7 Q7.2 8.8 9 9.6 L9.7 8.7 L11.7 9.2 L11.7 10.6 Q11.7 11.7 10.6 11.7 Q4.3 11.2 4.3 5.4 Q4.3 4.3 5.4 4.3 Z" fill="#fff"/>
      </svg>
      <span>587-412-6630</span>
    </div>
    <div class="person">
      <p class="person-name">Daniel Reyes</p>
      <p class="person-title">Co-Founder</p>
    </div>
    <p class="address">MeloraSkin, 14, 618 Birchmont Way, St. Albert, Alberta, K2P 7W3</p>
  </section>
</main>
</body>
</html>
```